Copper Hollow Sparkling

Hi all,

Thanks for taking the time to check out our brief.

Copper Hollow is an Australian wine company based in Victoria, and have been around for more than 20 years. We have a well-known sparkling Chardonnay Pinot Noir that needs a package revamp and we need your help!

Check out our current package here: http://www.copperhollowvino.com.au/our-wines/dsp-default_b.cfm?loadref=17

So here's the brief:

1. Use of the Copper Hollow logo (silhouette) and text mandatory - but can be as small/large as required.

2. Design must be shown on a sparkling bottle.

3. Can be closed with cork or crown seal - neck label/hood not mandatory.

4. Front label size to be no larger than 75mm high x 100mm wide. Back label to be no larger than 75mm x 100mm

5. Label does not have to be square/rectangular. Happy to see thoughts outside the box.

6. Design cannot be printed onto the bottle - must be on a label that can be applied to the bottle.

7. Be forward thinking. Be interesting. This design does not have to tie into our still (red and white) wine range.

8. Mandatory information to be shown on front label - a. Wine of Australia - b. Sparkling Chardonnay Pinot Noir

9. Mandatory info for front label - a. 750mL - b. Alcohol e.g. 13.5% ALC/VOL - c. Wine of Australi - d. Producer address (please insert dummy address at this stage - e. standard drinks e.g. approx 8.0 standard drinks (this can also be shown in the standard drinks glass logo) - f. space for a tasting blurb

10. Try to stay away from anything floral or overly girly.

Industry/Entity Type

Floral

Requirements
Must have
• Design must be shown on a sparkling wine bottle & include the full label design separately
Should not have
• Try to stay away from anything too floral and overly girly.

```html
<!DOCTYPE html>
<html lang="en">
<head>
<meta charset="utf-8">
<title>Copper Hollow Sparkling – Front Label</title>
<link rel="stylesheet" href="https://fonts.googleapis.com/css2?family=Cormorant+Garamond:wght@500&family=Great+Vibes&family=Roboto+Condensed:wght@400;700&display=swap">
<style>
  :root {
    --backdrop: #5a5a5c;
    --label-white: #ffffff;
    --ink: #231f20;
    --gold: #b8860b;
    --gold-dark: #7a5a10;
    --gold-light: #f6e27a;
    --silhouette: #ece7a0;
  }
  html, body {
    margin: 0;
    padding: 0;
    width: 1200px;
    height: 900px;
    overflow: hidden;
    background: var(--backdrop);
  }
  .label-canvas {
    display: block;
    width: 1200px;
    height: 900px;
  }
  .brand-name {
    font-family: "Cormorant Garamond", serif;
    font-weight: 500;
    font-size: 27px;
    letter-spacing: 7px;
    fill: var(--ink);
  }
  .origin-script {
    font-family: "Great Vibes", cursive;
    font-size: 92px;
    fill: url(#goldText);
  }
  .variety {
    font-family: "Roboto Condensed", sans-serif;
    font-size: 25px;
    letter-spacing: 3px;
    fill: var(--ink);
  }
  .producer-address,
  .fine-print {
    font-family: "Roboto Condensed", sans-serif;
    font-size: 12.5px;
    fill: var(--gold);
  }
  .fine-print strong { font-weight: 700; }
  .volume {
    font-family: "Roboto Condensed", sans-serif;
    font-weight: 700;
    font-size: 19px;
    fill: var(--gold-dark);
  }
</style>
</head>
<body>
<svg class="label-canvas" viewBox="0 0 1200 900" xmlns="http://www.w3.org/2000/svg">
  <defs>
    <linearGradient id="goldFrame" x1="0" y1="0" x2="1" y2="1">
      <stop offset="0" stop-color="#f8e873"/>
      <stop offset="0.25" stop-color="#b07a12"/>
      <stop offset="0.5" stop-color="#fff27a"/>
      <stop offset="0.75" stop-color="#8a5b0c"/>
      <stop offset="1" stop-color="#f4d34a"/>
    </linearGradient>
    <linearGradient id="goldText" x1="0" y1="0" x2="0" y2="1">
      <stop offset="0" stop-color="#f3d650"/>
      <stop offset="0.5" stop-color="#a8760f"/>
      <stop offset="1" stop-color="#e8c23a"/>
    </linearGradient>
    <filter id="labelShadow" x="-10%" y="-10%" width="120%" height="120%">
      <feDropShadow dx="0" dy="2" stdDeviation="3" flood-color="#000" flood-opacity="0.35"/>
    </filter>
    <path id="labelShape" d="M 470 222 Q 600 318 730 222 C 900 236 945 356 945 460 C 945 570 880 664 760 690 Q 600 520 440 690 C 320 664 255 570 255 460 C 255 350 310 236 470 222 Z"/>
  </defs>

  <!-- die-cut label -->
  <use href="#labelShape" class="label-body" fill="var(--label-white)" filter="url(#labelShadow)"/>
  <use href="#labelShape" class="label-frame" fill="none" stroke="url(#goldFrame)" stroke-width="7"
       transform="translate(600 458) scale(0.962 0.955) translate(-600 -458)"/>

  <!-- brand name -->
  <text class="brand-name" x="600" y="326" text-anchor="middle">COPPER HOLLOW</text>

  <!-- brand silhouette mark area -->
  <rect class="brand-silhouette" role="img" aria-label="Copper Hollow brand silhouette mark"
        x="512" y="334" width="178" height="276" rx="40" fill="var(--silhouette)" opacity="0.9"/>

  <!-- origin statement -->
  <text class="origin-script" x="588" y="474" text-anchor="middle">Wine of Australia</text>

  <!-- variety band -->
  <line class="rule" x1="282" y1="492" x2="918" y2="492" stroke="var(--gold)" stroke-width="1.2"/>
  <text class="variety" x="600" y="530" text-anchor="middle">SPARKLING CHARDONNAY PINOT NOIR</text>
  <line class="rule" x1="282" y1="549" x2="918" y2="549" stroke="var(--gold)" stroke-width="1.2"/>

  <text class="producer-address" x="600" y="571" text-anchor="middle">This dummy address at this stage Please don't read it. Thank you</text>

  <!-- volume -->
  <ellipse class="volume-badge" cx="746" cy="611" rx="32" ry="18" fill="none" stroke="var(--gold-dark)" stroke-width="1.5"/>
  <text class="volume" x="746" y="618" text-anchor="middle">750ml</text>

  <!-- statutory fine print -->
  <text class="fine-print standard-drinks" transform="translate(368 616) rotate(38)" text-anchor="middle">Approx <tspan font-weight="700">8.0</tspan> Standard Drinks</text>
  <text class="fine-print alcohol" transform="translate(832 624) rotate(-38)" text-anchor="middle">Alcohol e.g. 13.5% ALC/VOL</text>
</svg>
</body>
</html>
```